Simple fencing and steel manufacturing website

** update 01/04/2015 ** we did not add logo design, but if your font/logo is accepted we will add $50 to make it more fair
Even if you web design is not chosen, but your logo is, we will pay you $50. If both are chosen you will get an extra $50
Open brief

Site map:
Home
About
Gallery
-photos
-testimonials
Contact

No current website:

No current logo, colors currently black and gold but we don't mind changing them - wide open brief
Happy for new font/style/logo for company name which is Paling Brightway

Customer wants clean, credible and professional look & feel
stock photos OK

Brief:

One home page - simple with 2 or 3 small areas to tease and attract the user and one template page to suit all the other pages

All competitor websites are pretty bad, the best of them is
http://www.wexmoorrailing.com.au/index.html

Target Market(s)

Government and top level builders

Industry/Entity Type

Fencing

Requirements
Must have
• 1. Display ISO and environmental awards (ISO9001 AS4801 ISO14001)
• 2. A list of about 15 products
• Can be in teaser areas of home page as suggested before or slider or really anywhere
Nice to have
• Log with name - nice but not necessary (we don't have one)

```html
<!DOCTYPE html>
<html lang="en">
<head>
<meta charset="utf-8">
<title>Paling Brightway</title>
<link href="https://fonts.googleapis.com/css2?family=Oswald:wght@400;500&family=Roboto:ital,wght@0,400;0,500;1,400&family=PT+Serif:wght@700&display=swap" rel="stylesheet">
<style>
:root{
  --red:#c0302a;
  --red-dark:#a8251f;
  --black:#0d0d0d;
  --dark:#3a3a3a;
  --grey-text:#555;
  --light-line:#d6d6d6;
  --panel:#f2f2f2;
  --white:#fff;
}
*{box-sizing:border-box;margin:0;padding:0}
html,body{width:824px;height:1200px;overflow:hidden;background:var(--white)}
body{font-family:"Roboto",Arial,sans-serif;color:var(--grey-text);position:relative}
.abs{position:absolute}
.top-rule{left:0;top:0;width:824px;height:2px;background:var(--red)}
.social-top{left:629px;top:0;display:flex;gap:1px}
.social-top span{width:25px;height:25px;background:var(--red);display:block}
.brand{left:91px;top:44px;display:flex;align-items:center;gap:9px;font-family:"Oswald",sans-serif;font-weight:500;font-size:25px;color:var(--red);line-height:30px;letter-spacing:.3px}
.brand i{display:block;width:16px;height:16px;background:var(--red)}
.consult{left:437px;top:51px;width:164px;height:24px;background:var(--black);color:#fff;font-family:"PT Serif",serif;font-size:11px;font-weight:700;line-height:24px;text-align:center}
.call{left:619px;top:46px;display:flex;align-items:center;gap:6px}
.call svg{width:22px;height:22px}
.call small{display:block;color:var(--red);font-family:"PT Serif",serif;font-size:10px;font-weight:700}
.call strong{display:block;color:var(--red);font-family:"PT Serif",serif;font-size:15px;font-weight:700;line-height:16px}
.nav{left:0;top:96px;width:824px;height:33px;background:var(--black)}
.nav ul{list-style:none;display:flex;position:absolute;left:90px;top:0;height:33px}
.nav li{color:#fff;font-size:11px;font-weight:500;line-height:33px;text-align:center;border-right:1px solid #333}
.nav li.active{background:var(--red)}
.nav li:last-child{border-right:none}
.hero{left:0;top:129px;width:824px;height:312px;background:linear-gradient(180deg,#9a9ca0 0%,#c9cacd 45%,#8e9092 75%,#4c4d4f 100%)}
.hero-arrow{top:140px;width:14px;height:40px}
.caption{left:197px;top:324px;width:430px;height:53px;background:rgba(30,30,30,.8);color:#fff;font-family:"PT Serif",serif;font-weight:700;font-size:14.5px;line-height:21px;text-align:center;padding-top:5px}
.thumbs{left:0;top:377px;width:824px;height:64px;background:rgba(40,40,40,.55)}
.thumbs .row{position:absolute;left:92px;top:2px;display:flex;gap:6px}
.thumbs .row div{width:58px;height:60px;border:1px solid #ddd}
.thumbs .row div.sel{border:2px solid var(--red)}
.section-title{left:0;width:824px;text-align:center;font-family:"Oswald",sans-serif;font-size:15px;color:var(--red)}
.section-sub{left:0;width:824px;text-align:center;font-size:10px;color:var(--grey-text)}
.divider{height:12px}
.product-card{top:517px;width:198px;height:137px;box-shadow:0 6px 6px -4px rgba(0,0,0,.25)}
.product-card .label{position:absolute;left:2px;bottom:0;width:87px;height:21px;background:var(--red);color:#fff;font-family:"Oswald",sans-serif;font-size:13px;line-height:21px;padding-left:7px}
.box{top:685px;width:199px;height:207px;border-top:2px solid var(--red);border-left:1px solid #e2e2e2;border-right:1px solid #e2e2e2;border-bottom:1px solid #e2e2e2;background:#fff;box-shadow:0 8px 8px -6px rgba(0,0,0,.2)}
.box-head{position:absolute;left:7px;top:9px;display:flex;align-items:center;gap:6px;font-family:"Oswald",sans-serif;font-size:11.5px;color:var(--black)}
.box-head .icon{width:26px;height:26px;border-radius:50%;background:#ddd;display:flex;align-items:center;justify-content:center}
.box p{font-size:8.4px;line-height:13.5px;color:#333}
.read-more{position:absolute;right:10px;bottom:7px;font-size:7.5px;color:#111;font-weight:500}
.products-list{position:absolute;left:11px;top:47px;list-style:none}
.products-list li{font-size:8.3px;line-height:13.5px;color:#333;display:flex;align-items:center;gap:7px}
.products-list svg{width:9px;height:8px}
.field{position:absolute;left:9px;width:181px;height:20px;border:1px solid #ddd;font-size:7px;color:#aaa;padding:3px 6px}
.submit{position:absolute;left:9px;top:173px;width:76px;height:20px;background:var(--red);color:#fff;font-family:"Oswald",sans-serif;font-size:11.5px;line-height:20px;text-align:center}
.quote{left:96px;top:984px;width:548px;height:66px;background:var(--panel);padding:8px 14px 0 12px;font-style:italic;font-size:8.8px;line-height:16.5px;color:#333}
.quote .mark{font-family:"PT Serif",serif;font-style:normal;font-size:26px;color:#bbb;line-height:12px;vertical-align:-8px;margin-right:10px}
.avatar{left:646px;top:1001px;width:80px;height:80px;border-radius:50%;border:2px solid #b08a5a;background:radial-gradient(circle at 50% 40%,#d9e4ec,#7b9ab2)}
.reviewer{left:480px;top:1067px;width:155px;text-align:right;color:var(--red);font-style:italic;font-weight:500;font-size:8.5px}
.news{left:0;top:1105px;width:824px;height:45px;background:var(--red)}
.news-title{left:129px;top:1118px;color:#fff;font-size:15px}
.news-input{left:262px;top:1118px;width:167px;height:20px;background:#fff;font-size:8.5px;color:#666;line-height:20px;padding-left:21px}
.subscribe{left:429px;top:1118px;width:62px;height:20px;background:#2b2b2b;color:#fff;font-size:10px;font-weight:500;line-height:20px;text-align:center}
.follow{left:575px;top:1119px;display:flex;align-items:center;gap:6px;color:#fff;font-size:12.5px}
.follow span{width:20px;height:20px;border-radius:50%;background:#fff;display:block}
.footer{left:0;top:1150px;width:824px;height:50px;background:var(--dark)}
.footer-nav{left:93px;top:1159px;display:flex;list-style:none}
.footer-nav li{color:#fff;font-size:8.5px;font-weight:500;padding:0 9px;border-right:1px solid #666}
.footer-nav li:first-child{padding-left:0}
.footer-nav li:last-child{border:none}
.copyright{left:91px;top:1179px;font-size:7.5px;color:#bbb}
.we-are{left:540px;top:1159px;color:#fff;font-family:"Oswald",sans-serif;font-size:11px;line-height:15px}
.badges{left:567px;top:1156px;width:162px;height:36px;border-radius:18px;border:2px solid #ccc;display:flex;align-items:center;padding:0 3px;gap:2px}
.badges span{width:50px;height:28px;border-radius:14px;background:#8d8d8d;border:1px solid #ddd}
</style>
</head>
<body>
<div class="abs top-rule"></div>
<div class="abs social-top" aria-label="Social links"><span></span><span></span><span></span><span></span></div>

<div class="abs brand"><i></i>PALING BRIGHTWAY</div>
<div class="abs consult">Request For Free Consultation</div>
<div class="abs call">
  <svg viewBox="0 0 24 24"><circle cx="12" cy="12" r="10.5" fill="none" stroke="#c0302a" stroke-width="1.5"/><path d="M9 6c-1.5 1-2 3 0 7s4.5 5.5 6 5l1-1.5-2.5-2-1.2.8c-1-.7-2.6-3-2.8-4.2l1.2-.7-.6-3.2z" fill="#c0302a"/></svg>
  <div><small>Call Us Today</small><strong>123-456-7890</strong></div>
</div>

<nav class="abs nav">
  <ul>
    <li class="active" style="width:79px">HOME</li>
    <li style="width:97px">ABOUT US</li>
    <li style="width:109px">PRODUCTS</li>
    <li style="width:98px">GALLERY</li>
    <li style="width:166px">CLIENT TESTIMONIALS</li>
    <li style="width:114px">CONTACT US</li>
  </ul>
</nav>

<div class="abs hero" role="img" aria-label="Ornate wrought iron gate against a cloudy sky"></div>
<svg class="abs hero-arrow" style="left:66px" viewBox="0 0 14 40"><path d="M12 2 2 20l10 18" fill="none" stroke="#eee" stroke-width="2"/></svg>
<svg class="abs hero-arrow" style="left:746px" viewBox="0 0 14 40"><path d="M2 2l10 18L2 38" fill="none" stroke="#eee" stroke-width="2"/></svg>
<div class="abs caption">We Specialise In The Supply &amp; Installation Of Fencing For<br>Government, Residential &amp; Commercial Sectors</div>
<div class="abs thumbs">
  <div class="row">
    <div role="img" aria-label="Stadium seating" style="background:linear-gradient(#6fb85a,#2b5fb8)"></div>
    <div role="img" aria-label="Airport fence" style="background:linear-gradient(#8fc0e0,#d9b24a)"></div>
    <div role="img" aria-label="Running track" style="background:linear-gradient(#5a9a4a,#c24a3a)"></div>
    <div class="sel" role="img" aria-label="Iron gate" style="background:linear-gradient(#c8c8c8,#444)"></div>
    <div role="img" aria-label="Barbed wire fence at sunset" style="background:linear-gradient(#e8c15a,#9a7a30)"></div>
    <div role="img" aria-label="Palisade fence" style="background:linear-gradient(#5a6aa8,#e0b840)"></div>
    <div role="img" aria-label="Steel canopy" style="background:linear-gradient(#2e5ea8,#8fb8e0)"></div>
    <div role="img" aria-label="Sports field" style="background:linear-gradient(#e8ecf0,#7aa040)"></div>
    <div role="img" aria-label="Stadium fencing" style="background:linear-gradient(#b8ccdc,#6a8a5a)"></div>
    <div role="img" aria-label="Steel mesh roof" style="background:linear-gradient(#4a80c0,#2a4a90)"></div>
  </div>
</div>

<div class="abs section-title" style="top:456px">Types of Product We Offer</div>
<div class="abs section-sub" style="top:477px">Domestic Fencing Company Providing Services To Airport, Stadium, Schools...etc And Many Others.</div>
<svg class="abs divider" style="left:228px;top:493px;width:184px" viewBox="0 0 184 12"><line x1="0" y1="6" x2="184" y2="6" stroke="#ccc"/><rect x="72" y="0" width="40" height="12" fill="#fff"/><g fill="#c0302a"><polygon points="78,1 79.5,5 83.5,5 80.3,7.5 81.5,11 78,9 74.5,11 75.7,7.5 72.5,5 76.5,5"/><polygon points="92,1 93.5,5 97.5,5 94.3,7.5 95.5,11 92,9 88.5,11 89.7,7.5 86.5,5 90.5,5"/><polygon points="106,1 107.5,5 111.5,5 108.3,7.5 109.5,11 106,9 102.5,11 103.7,7.5 100.5,5 104.5,5"/></g></svg>

<div class="abs product-card" style="left:98px" role="img" aria-label="Barbed wire fence at sunset with aircraft"><div style="position:absolute;inset:0;background:linear-gradient(180deg,#c9b98a,#e6b545 55%,#7a6a3a)"></div><div class="label">FENCING</div></div>
<div class="abs product-card" style="left:315px" role="img" aria-label="Steel gate structure under blue canopy"><div style="position:absolute;inset:0;background:linear-gradient(180deg,#3a6fc0,#9cc0e6 60%,#5a7aa8)"></div><div class="label">GATES</div></div>
<div class="abs product-card" style="left:531px;top:520px" role="img" aria-label="Aluminium grandstand seating"><div style="position:absolute;inset:0;background:linear-gradient(180deg,#7fa8d8,#c4c8cc 55%,#a88a70)"></div><div class="label">ACCESSORIES</div></div>

<section class="abs box" style="left:90px">
  <div class="box-head"><div class="icon"><svg width="12" height="12" viewBox="0 0 12 12"><circle cx="6" cy="3.5" r="2.7" fill="#c0302a"/><path d="M1 12c0-4 2.2-5.5 5-5.5s5 1.5 5 5.5z" fill="#c0302a"/></svg></div>WELCOME TO PALING BRIGHTWAY</div>
  <div class="abs" style="left:9px;top:45px;width:181px;height:78px;background:linear-gradient(90deg,#e8edf0,#c8d2da 60%,#3a4e66)" role="img" aria-label="Smiling businessman at a desk"></div>
  <p class="abs" style="left:10px;top:130px;width:182px">Hendrerit in vulputate molestie consquatisi atvero eros et accumsan iustoodio ignissimr qui blandit praesent luptatulenit auedolore te feugait nulla facilisilestie consey.</p>
  <div class="read-more">READ MORE</div>
</section>

<section class="abs box" style="left:315px">
  <div class="box-head"><div class="icon"><svg width="16" height="10" viewBox="0 0 16 10"><g stroke="#c88" stroke-width="1"><line x1="0" y1="2" x2="16" y2="2"/><line x1="0" y1="5" x2="16" y2="5"/><line x1="0" y1="8" x2="16" y2="8"/></g></svg></div>OUR PRODUCTS</div>
  <ul class="products-list">
    <li><svg viewBox="0 0 9 8"><path d="M1 4l2.5 2.5L8 1" fill="none" stroke="#999" stroke-width="1.8"/></svg>Eminence</li>
    <li><svg viewBox="0 0 9 8"><path d="M1 4l2.5 2.5L8 1" fill="none" stroke="#999" stroke-width="1.8"/></svg>Palisade (EA and IE Spec.)</li>
    <li><svg viewBox="0 0 9 8"><path d="M1 4l2.5 2.5L8 1" fill="none" stroke="#999" stroke-width="1.8"/></svg>Chainwire</li>
    <li><svg viewBox="0 0 9 8"><path d="M1 4l2.5 2.5L8 1" fill="none" stroke="#999" stroke-width="1.8"/></svg>Security Mesh (358 Mesh)</li>
    <li><svg viewBox="0 0 9 8"><path d="M1 4l2.5 2.5L8 1" fill="none" stroke="#999" stroke-width="1.8"/></svg>RTA Pedestrian (Type 1 - 5)</li>
    <li><svg viewBox="0 0 9 8"><path d="M1 4l2.5 2.5L8 1" fill="none" stroke="#999" stroke-width="1.8"/></svg>Partitions</li>
    <li><svg viewBox="0 0 9 8"><path d="M1 4l2.5 2.5L8 1" fill="none" stroke="#999" stroke-width="1.8"/></svg>Sporting Enclosures</li>
    <li><svg viewBox="0 0 9 8"><path d="M1 4l2.5 2.5L8 1" fill="none" stroke="#999" stroke-width="1.8"/></svg>Tubular (Pool/Garden)</li>
    <li><svg viewBox="0 0 9 8"><path d="M1 4l2.5 2.5L8 1" fill="none" stroke="#999" stroke-width="1.8"/></svg>Balustrades</li>
    <li><svg viewBox="0 0 9 8"><path d="M1 4l2.5 2.5L8 1" fill="none" stroke="#999" stroke-width="1.8"/></svg>Privacy Screens</li>
    <li><svg viewBox="0 0 9 8"><path d="M1 4l2.5 2.5L8 1" fill="none" stroke="#999" stroke-width="1.8"/></svg>Tonecoat Steel</li>
  </ul>
  <div class="read-more">READ MORE</div>
</section>

<section class="abs box" style="left:537px">
  <div class="box-head"><div class="icon"><svg width="12" height="12" viewBox="0 0 24 24"><path d="M6 2c-3 2-4 6 0 13s9 9 12 8l2-3-5-4-2.4 1.6C10.6 16 7.4 11.4 7 9l2.4-1.4L8.2 1z" fill="#c0302a"/></svg></div>QUICK INQUIRY</div>
  <p class="abs" style="left:9px;top:46px;font-size:7.8px">Lorem ipsum dolor sit amet, consectetuer</p>
  <div class="field" style="top:64px">Name</div>
  <div class="field" style="top:88px">Email</div>
  <div class="field" style="top:112px">Phone</div>
  <div class="field" style="top:135px;height:34px">Message</div>
  <div class="submit">SUBMIT</div>
</section>

<div class="abs section-title" style="top:919px">Our Customer Reviews</div>
<div class="abs section-sub" style="top:940px">Lorem ipsum dolor sit amet, consectetur Donec a consequat mag&nbsp; Aenean eu velit&nbsp; Aenean sollicitudin</div>
<svg class="abs divider" style="left:244px;top:956px;width:336px" viewBox="0 0 336 12"><line x1="0" y1="6" x2="336" y2="6" stroke="#ccc"/><rect x="148" y="0" width="40" height="12" fill="#fff"/><g fill="#c0302a"><polygon points="154,1 155.5,5 159.5,5 156.3,7.5 157.5,11 154,9 150.5,11 151.7,7.5 148.5,5 152.5,5"/><polygon points="168,1 169.5,5 173.5,5 170.3,7.5 171.5,11 168,9 164.5,11 165.7,7.5 162.5,5 166.5,5"/><polygon points="182,1 183.5,5 187.5,5 184.3,7.5 185.5,11 182,9 178.5,11 179.7,7.5 176.5,5 180.5,5"/></g></svg>

<blockquote class="abs quote"><span class="mark">&ldquo;</span>Lorem sum dolor sit amet, consectetuer adipiscing elit, sed diam nonummy nibh euismod tincidunt ut laoreet re agn aliqam erat volutpat wisi enim ad minim veniam, quis nostrud exerci tation ullamcorper suscipit lobortis nisl ut aliquip modo conseuatis autem vel eum iriure dolor in hendrerit in vulputate velit esse molestie consequat, vel illum dolore eu.</blockquote>
<svg class="abs" style="left:580px;top:1050px" width="16" height="10" viewBox="0 0 16 10"><path d="M0 0h16L8 10z" fill="#f2f2f2"/></svg>
<div class="abs avatar" role="img" aria-label="Portrait of a satisfied customer"></div>
<div class="abs reviewer">Lorem ipsum, DOLOR</div>

<div class="abs news"></div>
<svg class="abs" style="left:90px;top:1111px" width="32" height="32" viewBox="0 0 32 32"><rect x="3" y="8" width="24" height="20" fill="#e8eef4" stroke="#fff"/><path d="M3 8l12 10 12-10" fill="none" stroke="#7a9ab8"/><line x1="30" y1="2" x2="16" y2="22" stroke="#333" stroke-width="2"/></svg>
<div class="abs news-title">Newsletter Signup</div>
<div class="abs news-input"><svg class="abs" style="left:7px;top:6px" width="10" height="8" viewBox="0 0 10 8"><rect x=".5" y=".5" width="9" height="7" fill="none" stroke="#888"/><path d="M.5.5l4.5 4 4.5-4" fill="none" stroke="#888"/></svg>Enter your email here</div>
<div class="abs subscribe">Subscribe</div>
<div class="abs follow">Follow Us <span></span><span></span><span></span><span></span></div>

<footer class="abs footer"></footer>
<ul class="abs footer-nav">
  <li>HOME</li><li>ABOUT US</li><li>PRODUCTS</li><li>GALLERY</li><li>TESTIMONIALS</li><li>CONTACT US</li>
</ul>
<div class="abs copyright">Copyright © 2015 PalingBrightway &nbsp;|&nbsp; All Rights Reserved &nbsp;|&nbsp; Terms &amp; Conditions</div>
<div class="abs we-are">We<br>Are</div>
<div class="abs badges" aria-label="Certifications"><span></span><span></span><span></span></div>
</body>
</html>
```